Herbal tea shop web designing - Brewvine

We need a business-charity purpose online shop selling premium herbal teas with a tagline "Healthy with a heart" where all the raw materials are being purchased from Indonesian local farmers in order to give them sustainable employment. Every 20% from the total amount of the customer's purchase from our website always goes back to their communities to help build better sanitation, education or whatever they need. We need page to blog too and another page for customers to interact and share their thought. we expect an eye catching simple earthy (maybe a bit rustic) design with some brush lettering font in some parts. Thank you.

Target Market(s)

-Tea Lovers
-Anyone with body weight issues or any health issues in general

Industry/Entity Type

Home Health Care

Number of Pages Required

5+ page

Font styles to use
Other font styles liked:
• brush lettering font in some parts

Requirements
Must have
• - Brush lettering font
• -Simple, a bit rustic design with some nice watercolor touch
• -Blogging Page
• -catchy yet fancy and elegant E-commerce page
Nice to have
• Well, I will let the designers use their skills and imaginations to the fullest.

```html
<!DOCTYPE html>
<html lang="en">
<head>
<meta charset="utf-8">
<title>Brewvine — Healthy with a heart</title>
<link href="https://fonts.googleapis.com/css2?family=Amatic+SC:wght@400;700&family=Quicksand:wght@300;400;500;700&display=swap" rel="stylesheet">
<style>
:root{
  --paper:#f3f3f1;
  --white:#fdfdfd;
  --ink:#2b2b2b;
  --muted:#9a9a9a;
  --sky:#8fcbeb;
  --sky-soft:#c3e3f5;
  --sky-deep:#6fb8df;
  --rule:#dedede;
  --panel:#1f3f3c;
}
*{box-sizing:border-box;margin:0;padding:0}
html,body{width:1200px;height:2862px;overflow:hidden}
body{background:var(--paper);font-family:"Quicksand",sans-serif;color:var(--ink);position:relative}
.abs{position:absolute}
.wash{position:absolute;border-radius:50%;filter:blur(6px)}
.wash-a{left:-120px;top:120px;width:300px;height:620px;background:radial-gradient(ellipse at center,rgba(143,203,235,.55),rgba(143,203,235,0) 70%);transform:rotate(-18deg)}
.wash-b{left:820px;top:-140px;width:520px;height:300px;background:radial-gradient(ellipse at center,rgba(143,203,235,.6),rgba(143,203,235,0) 70%);transform:rotate(20deg)}
.wash-c{left:1000px;top:950px;width:300px;height:900px;background:radial-gradient(ellipse at center,rgba(143,203,235,.6),rgba(143,203,235,0) 70%);transform:rotate(-10deg)}
.wash-d{left:-140px;top:2050px;width:320px;height:520px;background:radial-gradient(ellipse at center,rgba(143,203,235,.55),rgba(143,203,235,0) 70%)}

.social{display:flex;gap:8px}
.social span{width:26px;height:26px;border-radius:50%;background:var(--sky-deep);display:block}
.brand{font-family:"Amatic SC",cursive;font-weight:700;color:var(--sky);letter-spacing:3px}
.util{font-size:11px;letter-spacing:.5px;display:flex;align-items:center;gap:8px;text-transform:uppercase}
.header-rule{left:216px;width:769px;top:162px;border-top:1px solid var(--rule)}
.nav{top:196px;left:0;width:1200px;display:flex;justify-content:center;gap:0}
.nav a{font-size:13px;letter-spacing:1px;color:var(--ink);text-decoration:none;text-transform:uppercase}

.hero{left:216px;top:248px;width:769px;height:460px;background:radial-gradient(ellipse at 45% 40%,#c9d5b8,#7b8f5c 45%,#3e4a2c 80%,#2b3220)}
.hero-title{left:216px;width:769px;top:462px;text-align:center;font-weight:300;font-size:44px;color:#fff;letter-spacing:3px}
.btn-ghost{border:1.5px solid #fff;color:#fff;font-size:15px;letter-spacing:1px;display:flex;align-items:center;justify-content:center;text-transform:uppercase}
.dots{left:565px;top:671px;display:flex;gap:8px}
.dots span{width:7px;height:7px;border-radius:50%;background:rgba(255,255,255,.75)}

.section-title{left:216px;width:769px;text-align:center;font-family:"Amatic SC",cursive;font-size:46px;color:var(--sky);letter-spacing:2px;line-height:1}
.arrow{width:20px;height:20px}

.card{width:174px}
.card .photo{height:151px}
.card .name{margin-top:14px;color:var(--sky);font-weight:500;font-size:15px;letter-spacing:1px}
.card .desc{margin-top:5px;color:var(--muted);font-size:10px;letter-spacing:.4px}
.card .price{margin-top:12px;font-size:17px;color:#555;letter-spacing:.5px}
.card .add{margin-top:20px;width:103px;height:31px;border:1.5px solid var(--sky-deep);font-size:9px;letter-spacing:1px;display:flex;align-items:center;justify-content:center;text-transform:uppercase;color:#444;background:var(--white)}

.cause{left:216px;top:1324px;width:769px;height:338px;background:linear-gradient(100deg,#39512f,#6a8a3c 45%,#8aa450 70%,#5f7a34)}
.cause-panel{left:259px;top:1362px;width:342px;height:279px;background:rgba(24,54,54,.88);padding:38px 22px 0 22px;color:#fff}
.cause-panel h2{font-size:20px;font-weight:700;line-height:26px;letter-spacing:.8px}
.cause-panel p{margin-top:10px;font-size:12.5px;line-height:18px;color:#cfd8d6;letter-spacing:.3px}
.cause-panel .btn-ghost{margin-top:26px;width:136px;height:39px;font-size:13px;font-weight:700}

.newsletter{left:216px;top:2219px;width:769px;height:219px;background:linear-gradient(135deg,#c8e5f6,#b6dcf2 50%,#c9e6f6)}
.newsletter h2{position:absolute;top:30px;width:100%;text-align:center;font-family:"Amatic SC",cursive;font-size:46px;color:#fff;letter-spacing:2px;font-weight:400}
.field{top:120px;height:40px;border-bottom:1px solid rgba(255,255,255,.7);background:rgba(255,255,255,.18);font-size:10px;color:#fff;padding:14px 12px;letter-spacing:.5px}
.subscribe{left:602px;top:120px;width:113px;height:40px;background:var(--sky-deep);color:#fff;font-size:10px;font-weight:700;letter-spacing:1px;display:flex;align-items:center;justify-content:center;text-transform:uppercase}

.footer{left:0;top:2492px;width:1200px;height:370px;background:var(--white)}
.footer h3{font-size:11px;color:var(--sky-deep);letter-spacing:1.2px;font-weight:700;text-transform:uppercase}
.footer ul{list-style:none;margin-top:42px}
.footer li{font-size:12px;letter-spacing:1px;line-height:28px;text-transform:uppercase;color:var(--ink)}
.bottom-rule{left:0;width:1200px;top:2810px;border-top:1px solid var(--rule)}
.copy{left:0;width:1200px;top:2830px;text-align:center;font-size:9px;letter-spacing:.6px;color:#444}
</style>
</head>
<body>

<div class="wash wash-a" role="img" aria-label="Soft blue watercolor wash"></div>
<div class="wash wash-b" role="img" aria-label="Soft blue watercolor wash"></div>
<div class="wash wash-c" role="img" aria-label="Soft blue watercolor wash"></div>
<div class="wash wash-d" role="img" aria-label="Soft blue watercolor wash"></div>

<header>
  <div class="abs social" style="left:214px;top:97px"><span></span><span></span><span></span><span></span></div>
  <div class="abs brand" style="left:0;width:1200px;top:58px;text-align:center;font-size:80px;line-height:1">Brewvine</div>
  <div class="abs util" style="left:803px;top:98px">
    <svg width="18" height="22" viewBox="0 0 18 22" fill="none" stroke="var(--sky-deep)" stroke-width="1.5"><rect x="1.5" y="6" width="15" height="14.5"/><path d="M5.5 6V4a3.5 3.5 0 0 1 7 0v2"/></svg>Cart</div>
  <div class="abs util" style="left:887px;top:98px">
    <svg width="18" height="22" viewBox="0 0 18 22" fill="none" stroke="var(--sky-deep)" stroke-width="1.5"><rect x="1.5" y="1.5" width="15" height="19"/><path d="M5 7h8M5 11h8M5 15h8"/></svg>My Account</div>
  <div class="abs header-rule"></div>
  <nav class="abs nav">
    <a href="#" style="margin-right:46px">Home</a>
    <a href="#" style="margin-right:44px">About Us</a>
    <a href="#" style="margin-right:38px">Products</a>
    <a href="#" style="margin-right:36px">Store Location</a>
    <a href="#" style="margin-right:40px">FAQ'S</a>
    <a href="#">Contact Us</a>
  </nav>
</header>

<section>
  <div class="abs hero" role="img" aria-label="Glass cup of green herbal tea with fresh leaves and dried tea on a wooden table"></div>
  <div class="abs hero-title">Healthy with a heart</div>
  <div class="abs btn-ghost" style="left:532px;top:540px;width:138px;height:42px">Shop Now</div>
  <div class="abs dots"><span></span><span></span><span></span><span></span></div>
</section>

<section>
  <svg class="abs arrow" style="left:222px;top:816px" viewBox="0 0 20 20"><path d="M13 3l-7 7 7 7" fill="none" stroke="#111" stroke-width="2.5"/></svg>
  <div class="abs section-title" style="top:804px">Featured Products</div>
  <svg class="abs arrow" style="left:956px;top:816px" viewBox="0 0 20 20"><path d="M7 3l7 7-7 7" fill="none" stroke="#111" stroke-width="2.5"/></svg>

  <div class="abs card" style="left:225px;top:887px"><div class="photo" role="img" aria-label="Cup of herbal tea with mint leaves" style="background:linear-gradient(135deg,#c9b48a,#b8862e 50%,#6d5a2e)"></div><div class="name">Herbel Tea 1</div><div class="desc">Sed ut perspiciatis unde omnis</div><div class="price">$27.00</div><div class="add">Add to cart</div></div>
  <div class="abs card" style="left:416px;top:887px"><div class="photo" role="img" aria-label="Glass of tea with lime and mint" style="background:linear-gradient(135deg,#e8ddc8,#c79a3e 50%,#5f7d2f)"></div><div class="name">Herbel Tea 1</div><div class="desc">Sed ut perspiciatis unde omnis</div><div class="price">$27.00</div><div class="add">Add to cart</div></div>
  <div class="abs card" style="left:609px;top:887px"><div class="photo" role="img" aria-label="Cup of black tea with loose leaves" style="background:linear-gradient(180deg,#f6f3ee,#d08a3a 55%,#3a2a1a)"></div><div class="name">Herbel Tea 1</div><div class="desc">Sed ut perspiciatis unde omnis</div><div class="price">$27.00</div><div class="add">Add to cart</div></div>
  <div class="abs card" style="left:801px;top:887px"><div class="photo" role="img" aria-label="Cup of golden herbal tea on a purple cloth" style="background:linear-gradient(135deg,#7a4a5a,#c9952f 50%,#6b3a48)"></div><div class="name">Herbel Tea 1</div><div class="desc">Sed ut perspiciatis unde omnis</div><div class="price">$27.00</div><div class="add">Add to cart</div></div>
</section>

<section>
  <div class="abs cause" role="img" aria-label="Local farming family outdoors among green plants"></div>
  <div class="abs cause-panel">
    <h2>We give 20% from the total amount of the customer's purchase from our website</h2>
    <p>Always goes back to their communities to help build better sanitation, education or whatever they need.</p>
    <div class="btn-ghost">Shop Now</div>
  </div>
</section>

<section>
  <svg class="abs arrow" style="left:222px;top:1761px" viewBox="0 0 20 20"><path d="M13 3l-7 7 7 7" fill="none" stroke="#111" stroke-width="2.5"/></svg>
  <div class="abs section-title" style="top:1749px">New Arrivals</div>
  <svg class="abs arrow" style="left:956px;top:1761px" viewBox="0 0 20 20"><path d="M7 3l7 7-7 7" fill="none" stroke="#111" stroke-width="2.5"/></svg>

  <div class="abs card" style="left:225px;top:1832px"><div class="photo" role="img" aria-label="Cup of red tea with lemon and mint" style="background:linear-gradient(135deg,#1e1a14,#a8391e 50%,#4f7a2a)"></div><div class="name">Herbel Tea 1</div><div class="desc">Sed ut perspiciatis unde omnis</div><div class="price">$27.00</div><div class="add">Add to cart</div></div>
  <div class="abs card" style="left:416px;top:1832px"><div class="photo" role="img" aria-label="Dark tea in a glass with dried herbs" style="background:linear-gradient(135deg,#f1ede6,#3a1f12 45%,#b59a6a)"></div><div class="name">Herbel Tea 1</div><div class="desc">Sed ut perspiciatis unde omnis</div><div class="price">$27.00</div><div class="add">Add to cart</div></div>
  <div class="abs card" style="left:609px;top:1832px"><div class="photo" role="img" aria-label="Tea with lemon, honey and spices" style="background:linear-gradient(135deg,#f5efe4,#e2a94a 50%,#8a5a2a)"></div><div class="name">Herbel Tea 1</div><div class="desc">Sed ut perspiciatis unde omnis</div><div class="price">$27.00</div><div class="add">Add to cart</div></div>
  <div class="abs card" style="left:801px;top:1832px"><div class="photo" role="img" aria-label="Herbal tea on a rustic wooden table" style="background:linear-gradient(135deg,#8a8070,#6f7a3a 50%,#4a4234)"></div><div class="name">Herbel Tea 1</div><div class="desc">Sed ut perspiciatis unde omnis</div><div class="price">$27.00</div><div class="add">Add to cart</div></div>
</section>

<section class="abs newsletter">
  <h2>Subscribe for Newsletter</h2>
  <div class="abs field" style="left:30px;width:288px">Name</div>
  <div class="abs field" style="left:326px;width:265px">E-Mail</div>
  <div class="abs subscribe">Subscribe Now</div>
</section>

<footer class="abs footer">
  <div class="abs brand" style="left:229px;top:60px;font-size:52px;line-height:1">Brewvine</div>
  <div class="abs" style="left:401px;top:68px">
    <h3>Quick Links</h3>
    <ul><li>Home</li><li>About Us</li><li>Products</li><li>Store Location</li><li>FAQ'S</li><li>Contact Us</li></ul>
  </div>
  <div class="abs" style="left:599px;top:68px">
    <h3>Let Us Help You</h3>
    <ul><li>Your Account</li><li>Returns</li><li>100% Guaranteed</li><li>Our Assistant</li><li>Help</li></ul>
  </div>
  <div class="abs" style="left:824px;top:68px">
    <h3>Get To Know Us</h3>
    <ul><li>Careers</li><li>Press Releases</li><li>Gift A Smile</li></ul>
    <h3 style="margin-top:22px">Connect With Us</h3>
    <div class="social" style="margin-top:16px"><span></span><span></span><span></span><span></span></div>
  </div>
</footer>
<div class="abs bottom-rule"></div>
<div class="abs copy">© 2017 BREWVINE | ALL RIGHTS RESERVED</div>

</body>
</html>
```